Company Stationary

I'd like a template to use for company stationery. We frequently write short 1 - 2 page Word documents (which we save as PDF) to clients and prospects and the presentation is boring and doesn't look professional. I am looking for a Word template that will convey a better sense of professionalism. The design should include our logo (attached) but be simple and elegant. It should save nicely as a PDF, since that is how we will send the files via email.

Target Market(s)

Financial Institutions

Industry/Entity Type

Financial Service

Font styles to use
Serif

Colors

Designer to choose colors to be used in the design.

Requirements
Must have
• Simple design. Needs to be subtle. I don't want the design to be more interesting than the message we are writing.
Nice to have
• When the reader sees it, I want them to feel they are reading something published by a large, very successful company.
Should not have
• Not overpowering design and colors.

```html
<!DOCTYPE html>
<html lang="en">
<head>
<meta charset="utf-8">
<title>Clarivane Letterhead</title>
<link rel="stylesheet" href="https://fonts.googleapis.com/css2?family=Open+Sans:wght@400;700;800&display=swap">
<style>
  :root {
    --ink: #111111;
    --paper: #ffffff;
    --accent: #f0292b;
    --footer-bg: #2b2f33;
    --footer-text: #f2f2f2;
  }
  * { margin: 0; padding: 0; box-sizing: border-box; }
  html, body {
    width: 1000px;
    height: 1200px;
    overflow: hidden;
    background: var(--paper);
    font-family: "Open Sans", Arial, sans-serif;
    color: var(--ink);
  }
  .letterhead {
    position: relative;
    width: 1000px;
    height: 1200px;
    background: var(--paper);
  }
  .masthead {
    position: absolute;
    top: 0; left: 0;
    width: 1000px;
    height: 165px;
  }
  .brand-name {
    position: absolute;
    left: 52px;
    top: 52px;
    font-size: 56px;
    font-weight: 800;
    letter-spacing: 0.5px;
    line-height: 1;
    color: var(--ink);
  }
  .contact {
    position: absolute;
    right: 31px;
    top: 48px;
    text-align: right;
    font-size: 16px;
    line-height: 39px;
    color: var(--ink);
  }
  .accent-rule {
    position: absolute;
    top: 165px; left: 0;
    width: 1000px;
    height: 12px;
    background: var(--accent);
  }
  .letter-body {
    position: absolute;
    top: 177px; left: 0;
    width: 1000px;
    height: 958px;
  }
  .footer {
    position: absolute;
    left: 0; bottom: 0;
    width: 1000px;
    height: 65px;
    background: var(--footer-bg);
    color: var(--footer-text);
    font-size: 16px;
  }
  .footer-copyright {
    position: absolute;
    left: 41px;
    top: 23px;
  }
  .footer-web {
    position: absolute;
    left: 410px;
    top: 23px;
  }
  .footer-brand {
    position: absolute;
    right: 43px;
    top: 16px;
    font-size: 26px;
    font-weight: 800;
    color: var(--footer-text);
  }
</style>
</head>
<body>
  <div class="letterhead">
    <header class="masthead">
      <div class="brand-name">Clarivane</div>
      <address class="contact" style="font-style: normal;">
        <div>218 Orchard Lane, Fairhaven, NJ 07510</div>
        <div>(555) 014-2280 • info@clarivane.com</div>
      </address>
    </header>
    <div class="accent-rule"></div>
    <main class="letter-body"></main>
    <footer class="footer">
      <span class="footer-copyright">© 2017 Clarivane, LLC</span>
      <span class="footer-web">www.clarivane.com</span>
      <span class="footer-brand">Clarivane</span>
    </footer>
  </div>
</body>
</html>
```